Velmira Construction Company Catalogue Design Project

looking for construction company catalog design, elegant, modern and shick

i made the project guaranteed for payment, waiting for serious designers. 

Reason: just made the project payment guaranteed/ so i am extending the deadline for another week.

Target Market(s)

ages 35 to 70 married couples

Industry/Entity Type

Construction

Requirements
Must have
• it should not look tacky with bunch of colors with cheesy layouts.

modern elegant shick page layout, construction company catalog showing company info and previous reference projects.

the catalog will be bound to 8.5x11" letter paper (or A4 europe)

the company info can be reached at http://www.velmira-build.example/English/

```html
<!DOCTYPE html>
<html lang="tr">
<head>
<meta charset="UTF-8">
<title>Velmira – Kurumsal Sayfa</title>
<link href="https://fonts.googleapis.com/css2?family=Source+Sans+3:wght@400;600;700&display=swap" rel="stylesheet">
<style>
  :root {
    --backdrop: #e8e5e0;
    --page-top: #6c100d;
    --page-mid: #3a0606;
    --page-bottom: #0c0000;
    --text-light: #f6eeee;
    --watermark: rgba(140, 50, 40, 0.32);
    --footer-bg: #ffffff;
    --brand-ink: #1c1c1c;
    --brand-accent: #c8161d;
  }
  * { margin: 0; padding: 0; box-sizing: border-box; }
  html, body {
    width: 1200px; height: 960px; overflow: hidden;
    background: var(--backdrop);
    font-family: "Source Sans 3", "Myriad Pro", sans-serif;
  }
  .page {
    position: absolute; left: 252px; top: 30px;
    width: 696px; height: 900px;
    background: linear-gradient(180deg, var(--page-top) 0%, var(--page-mid) 45%, var(--page-bottom) 100%);
    box-shadow: 2px 3px 8px rgba(0,0,0,0.35);
  }
  .watermark {
    position: absolute; left: 60px; right: 40px; top: 382px;
    text-align: center;
    font-size: 82px; font-weight: 700; letter-spacing: 6px;
    color: var(--watermark);
    pointer-events: none;
  }
  .principles {
    position: absolute; left: 66px; top: 106px; width: 580px;
    list-style: none;
  }
  .principles li {
    position: relative; padding-left: 32px;
    color: var(--text-light);
    font-size: 18px; line-height: 24.5px;
    margin-bottom: 24.5px;
  }
  .principles li::before {
    content: ""; position: absolute; left: 0; top: 5px;
    width: 15px; height: 15px; border-radius: 50%;
    background: #ffffff;
  }
  .page-footer {
    position: absolute; left: 0; bottom: 0;
    width: 100%; height: 62px;
    background: var(--footer-bg);
  }
  .brand {
    position: absolute; right: 32px; top: 20px;
    display: flex; align-items: center; gap: 7px;
  }
  .brand-dot {
    width: 12px; height: 12px; border-radius: 50%;
    background: var(--brand-accent);
  }
  .brand-name {
    font-size: 17px; font-weight: 700; letter-spacing: 1.5px;
    color: var(--brand-ink);
  }
</style>
</head>
<body>
  <main class="page">
    <div class="watermark" aria-hidden="true">VELMIRA</div>
    <ul class="principles">
      <li>Dünyanın hızla artan nüfusu, değişen hayat temposu ve öngörülmesi güç teknolojik ilerlemeleri gözönüne alındığında mevcut yapı stoğunun sadece nicelik olarak değil, nitelik olarak da yetersiz kaldığı aşikardır.</li>
      <li>Son yıllarda dünyanın en hızlı büyüyen ekonomilerinden birine sahip olan ülkemizde inşaat sektörünün yıllardan beri lokomotif rolü oynadığı bilinmektedir.</li>
      <li>VELMIRA olarak bu sektörün yarattığı hızlı değişim ve gelişimin içinde uzun yıllardır yer almaktan ve katkıda bulunmaktan gururluyuz.</li>
      <li>İnşaat, taahhüt ve mühendislik alanlarının uzman bir kuruluşu olarak; öncelikli hedefimiz insan mutluluğu ve buna hizmet eden çözümler üretmek ve projelere imza atmaktır.</li>
      <li>Yurt içi ve yurt dışı anahtar teslimi genel müteahhitlik ve gayrimenkul geliştirme hizmetlerimizi dünya standartlarına uygun, yenilikçi, rekabetçi, sürekli gelişim peşinde, kaynakların kullanımında verimli, ve insan ve doğa dostu bir anlayış benimsemiş olarak icra etmekteyiz.</li>
      <li>Müşteri ihtiyaçlarına en iyi şekilde cevap verme, çözüm üretme, kurumsallaşma, sürekli gelişen bir kadro ile kalıcı olma, iş prensiplerimiz arasındadır.</li>
    </ul>
    <footer class="page-footer">
      <div class="brand">
        <span class="brand-dot"></span>
        <span class="brand-name">VELMIRA</span>
      </div>
    </footer>
  </main>
</body>
</html>
```